Graphics for a 'Hue Hunt' mobile phone project

I need the graphics (including source graphics in Illustrator or Photoshop) for the screens inside the game.

Please read the attached brief carefully, thanks!

```html
<!DOCTYPE html>
<html lang="en">
<head>
<meta charset="utf-8">
<title>Hue Hunt – Level Select</title>
<link href="https://fonts.googleapis.com/css2?family=Cinzel:wght@600;700&display=swap" rel="stylesheet">
<style>
  :root{
    --toolbar-bg:#efefef;
    --header-bg:#2b2b2b;
    --list-bg:#1e1e1e;
    --cell-bg:#ffffff;
    --ink:#1a1a1a;
    --light-ink:#ffffff;
    --btn-star:#1cb8e0;
    --btn-gear:#6cc012;
    --btn-sound:#c8141c;
    --btn-cart:#9c1ed2;
    --lvl-1:#7ed000;
    --lvl-2:#00c6e0;
    --lvl-3:#0a72e0;
    --lvl-4:#8a14e2;
    --lvl-5:#f01a9c;
    --lvl-6:#ee1428;
    --lvl-7:#f25e12;
    --lvl-8:#363636;
  }
  *{margin:0;padding:0;box-sizing:border-box}
  html,body{width:859px;height:1200px;overflow:hidden;background:var(--list-bg)}
  .screen{position:relative;width:859px;height:1200px;background:var(--list-bg);font-family:'Cinzel',serif}
  .toolbar{height:97px;background:var(--toolbar-bg);display:flex;justify-content:center;align-items:center;gap:40px}
  .tool-btn{width:72px;height:66px;border-radius:8px;display:flex;align-items:center;justify-content:center;box-shadow:inset 0 -5px 0 rgba(0,0,0,.22),0 2px 3px rgba(0,0,0,.25)}
  .tool-btn svg{width:30px;height:30px}
  .tool-btn.star{background:var(--btn-star)}
  .tool-btn.gear{background:var(--btn-gear)}
  .tool-btn.sound{background:var(--btn-sound)}
  .tool-btn.cart{background:var(--btn-cart)}
  .header{height:243px;background:var(--header-bg);display:flex;align-items:center;justify-content:center;gap:22px;padding-top:20px}
  .brand-mark{width:34px;height:34px;border-radius:50%;background:var(--lvl-2)}
  .brand-name{font-family:'Cinzel',serif;font-weight:700;font-size:72px;line-height:1;color:var(--light-ink);letter-spacing:2px}
  .levels{list-style:none;padding-top:2px}
  .level{display:flex;height:93px;margin-bottom:14px;box-shadow:0 6px 8px rgba(0,0,0,.5)}
  .level-num{width:196px;background:var(--cell-bg);color:var(--ink);display:flex;align-items:center;justify-content:center;font-size:34px;font-weight:600}
  .level-bar{flex:1;display:flex;align-items:center;justify-content:space-between;padding:0 26px;font-size:36px;font-weight:600;color:var(--ink);font-variant:small-caps;letter-spacing:2px;background-image:linear-gradient(180deg,rgba(255,255,255,.12),rgba(0,0,0,.08))}
  .level-bar.light{color:var(--light-ink)}
  .play{width:60px;height:60px}
  .lock{width:40px;height:48px;margin-right:8px}
</style>
</head>
<body>
<div class="screen">
  <nav class="toolbar">
    <div class="tool-btn star"><svg viewBox="0 0 24 24"><path fill="#111" d="M12 2l3 6.6 7 .8-5.2 4.8 1.5 7L12 17.7 5.7 21.2l1.5-7L2 9.4l7-.8z"/></svg></div>
    <div class="tool-btn gear"><svg viewBox="0 0 24 24"><g fill="#111"><circle cx="12" cy="12" r="6.5"/><rect x="10.5" y="2" width="3" height="20"/><rect x="2" y="10.5" width="20" height="3"/><rect x="10.5" y="2" width="3" height="20" transform="rotate(45 12 12)"/><rect x="10.5" y="2" width="3" height="20" transform="rotate(-45 12 12)"/></g><circle cx="12" cy="12" r="2.6" fill="#6cc012"/></svg></div>
    <div class="tool-btn sound"><svg viewBox="0 0 24 24"><path fill="#111" d="M3 9h4l5-4v14l-5-4H3z"/><path fill="none" stroke="#111" stroke-width="2" d="M15 9a4 4 0 010 6M17.5 6.5a7.5 7.5 0 010 11"/></svg></div>
    <div class="tool-btn cart"><svg viewBox="0 0 24 24"><path fill="none" stroke="#111" stroke-width="2" d="M2 4h3l2.5 11h11l2-8H6.5"/><circle cx="9" cy="19" r="1.8" fill="#111"/><circle cx="17" cy="19" r="1.8" fill="#111"/></svg></div>
  </nav>
  <header class="header">
    <span class="brand-mark"></span>
    <h1 class="brand-name">Hue Hunt</h1>
  </header>
  <ol class="levels">
    <li class="level"><div class="level-num">1</div><div class="level-bar" style="background-color:var(--lvl-1)">Level 1<svg class="play" viewBox="0 0 40 40"><circle cx="20" cy="20" r="17" fill="none" stroke="#fff" stroke-width="2.5"/><path fill="#fff" d="M13 10l17 10-17 10 5-10z"/></svg></div></li>
    <li class="level"><div class="level-num">2</div><div class="level-bar" style="background-color:var(--lvl-2)">Level 2<svg class="lock" viewBox="0 0 20 24"><path fill="none" stroke="#000" stroke-width="2.4" d="M5 11V7a5 5 0 0110 0v4"/><rect x="2" y="11" width="16" height="12" rx="1.5" fill="#000"/></svg></div></li>
    <li class="level"><div class="level-num">3</div><div class="level-bar" style="background-color:var(--lvl-3)">Level 3<svg class="lock" viewBox="0 0 20 24"><path fill="none" stroke="#000" stroke-width="2.4" d="M5 11V7a5 5 0 0110 0v4"/><rect x="2" y="11" width="16" height="12" rx="1.5" fill="#000"/></svg></div></li>
    <li class="level"><div class="level-num">4</div><div class="level-bar" style="background-color:var(--lvl-4)">Level 4<svg class="lock" viewBox="0 0 20 24"><path fill="none" stroke="#000" stroke-width="2.4" d="M5 11V7a5 5 0 0110 0v4"/><rect x="2" y="11" width="16" height="12" rx="1.5" fill="#000"/></svg></div></li>
    <li class="level"><div class="level-num">5</div><div class="level-bar light" style="background-color:var(--lvl-5)">Level 5<svg class="lock" viewBox="0 0 20 24"><path fill="none" stroke="#000" stroke-width="2.4" d="M5 11V7a5 5 0 0110 0v4"/><rect x="2" y="11" width="16" height="12" rx="1.5" fill="#000"/></svg></div></li>
    <li class="level"><div class="level-num">6</div><div class="level-bar light" style="background-color:var(--lvl-6)">Level 6<svg class="lock" viewBox="0 0 20 24"><path fill="none" stroke="#000" stroke-width="2.4" d="M5 11V7a5 5 0 0110 0v4"/><rect x="2" y="11" width="16" height="12" rx="1.5" fill="#000"/></svg></div></li>
    <li class="level"><div class="level-num">7</div><div class="level-bar light" style="background-color:var(--lvl-7)">Level 7<svg class="lock" viewBox="0 0 20 24"><path fill="none" stroke="#000" stroke-width="2.4" d="M5 11V7a5 5 0 0110 0v4"/><rect x="2" y="11" width="16" height="12" rx="1.5" fill="#000"/></svg></div></li>
    <li class="level"><div class="level-num">8</div><div class="level-bar light" style="background-color:var(--lvl-8)">Level 8<svg class="lock" viewBox="0 0 20 24"><path fill="none" stroke="#000" stroke-width="2.4" d="M5 11V7a5 5 0 0110 0v4"/><rect x="2" y="11" width="16" height="12" rx="1.5" fill="#000"/></svg></div></li>
  </ol>
</div>
</body>
</html>
```